KVRT PowerPoint Presentation

Professional Power point presentation .

KVRT Systems is an Quilmere Gold Partner. Uploading KVRT and Quilmere Partner logos to be available on the ppt.

Please use Arial Font

Industry/Entity Type

It Professional

```html
<!DOCTYPE html>
<html lang="en">
<head>
<meta charset="utf-8">
<title>KVRT Presentation Template</title>
<link rel="stylesheet" href="https://fonts.googleapis.com/css2?family=Arimo:wght@400;700&display=swap">
<style>
:root{
  --board:#d4d6d9;
  --blue:#0a57b5;
  --blue-dark:#084a9c;
  --green:#8dc63f;
  --text:#555a60;
  --muted:#8a8f95;
  --bar:#c9cbce;
  --white:#ffffff;
  --rule:#b9bcc0;
  --badge:#c8222b;
}
*{margin:0;padding:0;box-sizing:border-box}
html,body{width:1200px;height:899px;overflow:hidden;background:var(--board)}
body{font-family:"Arimo",Arial,sans-serif;color:var(--text);position:relative}
.slide{position:absolute;width:359px;height:277px;background:var(--white);overflow:hidden}
.col-1{left:51px}.col-2{left:425px}.col-3{left:797px}
.row-1{top:20px}.row-2{top:314px}.row-3{top:605px}
.slide-header{position:absolute;left:0;top:0;width:100%;height:23px;background:var(--blue);border-bottom:2px solid var(--green);color:var(--white);font-size:13px;line-height:23px;padding-left:17px;letter-spacing:.2px}
.slide-footer{position:absolute;left:17px;right:17px;top:261px;border-top:1px solid var(--rule)}
.footer-brand{position:absolute;left:0;top:3px;font-size:7px;font-weight:700;color:var(--blue);display:flex;align-items:center;gap:2px}
.footer-brand .dot{width:5px;height:5px;border-radius:50%;background:var(--green)}
.page-no{position:absolute;right:0;top:2px;font-size:5px;color:var(--muted)}
.body-text{font-size:5.6px;line-height:9.6px;color:var(--text);text-align:justify}
.caps-blue{font-size:5.8px;line-height:9.5px;color:var(--blue);text-transform:uppercase}

/* title slide */
.title-slide{background:var(--blue)}
.title-band{position:absolute;left:0;top:211px;width:100%;height:38px;background:var(--white);border-bottom:3px solid var(--green)}
.title-band h1{position:absolute;right:14px;top:8px;font-size:16px;font-weight:400;color:var(--blue-dark)}
.title-band p{position:absolute;right:17px;top:28px;font-size:7px;letter-spacing:5px;color:var(--muted)}
.brand-lockup{position:absolute;left:33px;top:52px}
.brand-name{display:flex;align-items:center;gap:6px;font-size:28px;font-weight:400;color:var(--white);line-height:1}
.brand-name .mark{width:14px;height:14px;border-radius:50%;background:var(--green)}
.partner-badge{margin-left:42px;margin-top:6px;width:60px;height:14px;background:var(--badge)}

/* agenda */
.agenda-list{position:absolute;left:61px;top:56px;list-style:none}
.agenda-list li{position:relative;height:20.2px}
.agenda-num{position:absolute;left:0;top:0;width:15px;height:15px;border-radius:50%;background:var(--blue);color:var(--white);font-size:8px;line-height:15px;text-align:center}
.agenda-bar{position:absolute;left:15px;top:1px;width:214px;height:13px;background:var(--bar);font-size:5.8px;line-height:13px;padding-left:12px;color:#5b6066}

/* about */
.team-photo{position:absolute;left:19px;top:40px;width:323px;height:75px;background:linear-gradient(90deg,#9ea1a5,#e4e5e6 45%,#b3b5b8 70%,#ececed)}
.about-lead{position:absolute;left:19px;top:127px;width:110px}
.about-body{position:absolute;left:138px;top:127px;width:201px}
.about-body p+p{margin-top:9px}

/* bullets */
.bullet-list{position:absolute;left:55px;top:64px;width:276px;list-style:none}
.bullet-list li{position:relative;padding-left:9px;margin-bottom:10px}
.bullet-list svg{position:absolute;left:0;top:1px}
.bullet-title{font-size:5.8px;line-height:9.6px;color:var(--blue)}

/* general */
.general-lead{position:absolute;left:14px;top:120px;width:104px;text-align:center}
.general-rule{position:absolute;left:128px;top:68px;width:1px;height:164px;background:var(--green)}
.general-body{position:absolute;left:142px;top:94px;width:185px}
.general-body p+p{margin-top:9px}

/* team */
.team-intro{position:absolute;left:40px;right:40px;top:56px;font-size:5.6px;line-height:9.6px;text-align:center;color:var(--muted)}
.member{position:absolute;top:89px;width:74px;text-align:center}
.member-photo{width:52px;height:52px;margin:0 auto;border-radius:50%;border:2px solid var(--blue);background:radial-gradient(circle at 50% 40%,#e8e9ea,#9fa3a7)}
.member h3{margin-top:10px;font-size:7px;font-weight:400;color:var(--blue)}
.member .role{font-size:5px;color:var(--muted);margin-top:1px}
.member .body-text{margin-top:6px;color:var(--muted);text-align:justify}

/* image text */
.image-slide{background:var(--blue)}
.image-slide h2{position:absolute;left:13px;top:16px;font-size:13px;font-weight:400;color:var(--white)}
.image-copy{position:absolute;left:22px;top:95px;width:133px}
.image-copy h3{font-size:5.8px;font-weight:400;color:var(--green);margin-bottom:6px}
.image-copy .body-text{color:#dce6f4}
.image-copy p+p{margin-top:6px}
.portrait{position:absolute;left:183px;top:0;width:176px;height:277px;background:linear-gradient(135deg,#5a5d61,#cfd1d3 45%,#f2f2f2 60%,#2d2f32)}
.image-brand{position:absolute;left:10px;top:260px;font-size:9px;font-weight:700;color:var(--white)}

/* section */
.section-slide{background:linear-gradient(160deg,#2a6cc0,#1559b0 50%,#0d4fa5)}
.section-icon{position:absolute;left:150px;top:124px;width:46px;height:46px;border-radius:50%;background:var(--white);color:var(--blue);font:italic 700 30px/46px Georgia,serif;text-align:center}
.section-rule{position:absolute;left:121px;top:178px;width:103px;height:1px;background:#d8e3f3}
.section-title{position:absolute;left:0;width:100%;top:184px;text-align:center;color:var(--green);font-size:13px}

/* thanks */
.thanks-top{position:absolute;left:0;top:0;width:100%;height:102px;background:var(--white);border-bottom:2px solid #8d949c}
.thanks-brand{position:absolute;left:24px;top:38px;display:flex;align-items:center;gap:8px;font-size:34px;color:var(--blue);line-height:1}
.thanks-brand .mark{width:18px;height:18px;border-radius:50%;background:var(--green)}
.thanks-panel{position:absolute;left:0;top:104px;width:100%;height:173px;background:var(--blue);border-bottom:3px solid var(--green)}
.thanks-panel h2{position:absolute;left:22px;top:21px;font-size:13px;font-weight:400;color:var(--green)}
.thanks-panel .sub{position:absolute;left:24px;top:40px;font-size:7px;color:var(--white)}
.contact-list{position:absolute;left:24px;top:95px;list-style:none;color:var(--white);font-size:5.8px;line-height:7.5px}
.contact-list li{display:flex;align-items:flex-start;gap:4px;margin-bottom:7px}
.contact-list svg{flex:none;margin-top:0}
</style>
</head>
<body>

<section class="slide col-1 row-1 title-slide">
  <div class="brand-lockup">
    <div class="brand-name"><span class="mark"></span>KVRT</div>
    <div class="partner-badge" role="img" aria-label="Quilmere Gold Partner badge"></div>
  </div>
  <div class="title-band">
    <h1>WELCOME TO</h1>
    <p>OUR PRESENTATION</p>
  </div>
</section>

<section class="slide col-2 row-1">
  <h2 class="slide-header">AGENDA</h2>
  <ol class="agenda-list">
    <li><span class="agenda-num">1</span><span class="agenda-bar">LOREM IPSUM DOLOR SIT MET LOREM IPSUM</span></li>
    <li><span class="agenda-num">2</span><span class="agenda-bar">LOREM IPSUM DOLOR SIT MET LOREM IPSUM</span></li>
    <li><span class="agenda-num">3</span><span class="agenda-bar">LOREM IPSUM DOLOR SIT MET LOREM IPSUM</span></li>
    <li><span class="agenda-num">4</span><span class="agenda-bar">LOREM IPSUM DOLOR SIT MET LOREM IPSUM</span></li>
    <li><span class="agenda-num">5</span><span class="agenda-bar">LOREM IPSUM DOLOR SIT MET LOREM IPSUM</span></li>
    <li><span class="agenda-num">6</span><span class="agenda-bar">LOREM IPSUM DOLOR SIT MET LOREM IPSUM</span></li>
    <li><span class="agenda-num">7</span><span class="agenda-bar">LOREM IPSUM DOLOR SIT MET LOREM IPSUM</span></li>
    <li><span class="agenda-num">8</span><span class="agenda-bar">LOREM IPSUM DOLOR SIT MET LOREM IPSUM</span></li>
    <li><span class="agenda-num">9</span><span class="agenda-bar">LOREM IPSUM DOLOR SIT MET LOREM IPSUM</span></li>
    <li><span class="agenda-num">10</span><span class="agenda-bar">LOREM IPSUM DOLOR SIT MET LOREM IPSUM</span></li>
  </ol>
  <footer class="slide-footer"><span class="footer-brand"><span class="dot"></span>KVRT</span><span class="page-no">12</span></footer>
</section>

<section class="slide col-3 row-1">
  <h2 class="slide-header">ABOUT US</h2>
  <div class="team-photo" role="img" aria-label="Black and white photo of a business team at work"></div>
  <p class="about-lead caps-blue">Lorem ipsum dolor sit met consectur adipisicing elit, sed do euismod tempor incididunt ut labore et delore magna</p>
  <div class="about-body body-text">
    <p>Lorem ipsum dolor sit amet, consectetur adipisicing elit, sed do eiusmod tempor incididunt ut labore et dolore magna aliqua. Ut enim ad minim veniam, quis nostrud exercitation ullamco laboris nisi ut aliquip ex ea commodo consequat. Duis aute irure dolor in reprehenderit in voluptate velit esse cillum dolore eu fugiat nulla pariatur.</p>
    <p>Lorem ipsum dolor sit amet, consectetur adipisicing elit, sed do eiusmod tempor incididunt ut labore et dolore magna aliqua. Ut enim ad minim veniam, quis nostrud exercitation ullamco laboris nisi ut aliquip ex ea commodo consequat. Duis aute irure dolor in reprehenderit in voluptate velit esse cillum dolore eu</p>
  </div>
  <footer class="slide-footer"><span class="footer-brand"><span class="dot"></span>KVRT</span><span class="page-no">12</span></footer>
</section>

<section class="slide col-1 row-2">
  <h2 class="slide-header">BULLET TEXT</h2>
  <ul class="bullet-list">
    <li>
      <svg width="6" height="6" viewBox="0 0 6 6"><rect x="0.3" y="0.3" width="5.4" height="5.4" fill="none" stroke="#0a57b5" stroke-width="0.6"/><path d="M1.2 3l1.2 1.3L4.9 1.6" fill="none" stroke="#0a57b5" stroke-width="0.9"/></svg>
      <p class="bullet-title">Lorem ipsum dolor sit amet</p>
      <p class="body-text">consectetur adipisicing elit, sed do eiusmod tempor incididunt ut labore et dolore magna aliqua. Ut enim ad minim veniam, quis nostrud exercitation ullamco laboris nisi ut aliquip ex ea commodo consequat. Duis aute irure dolor in reprehenderit in voluptate velit esse cillum dolore eu</p>
    </li>
    <li>
      <svg width="6" height="6" viewBox="0 0 6 6"><rect x="0.3" y="0.3" width="5.4" height="5.4" fill="none" stroke="#0a57b5" stroke-width="0.6"/><path d="M1.2 3l1.2 1.3L4.9 1.6" fill="none" stroke="#0a57b5" stroke-width="0.9"/></svg>
      <p class="bullet-title">Lorem ipsum dolor sit amet</p>
      <p class="body-text">consectetur adipisicing elit, sed do eiusmod tempor incididunt ut labore et dolore magna aliqua. Ut enim ad minim veniam, quis nostrud exercitation ullamco laboris nisi ut aliquip ex ea commodo consequat. Duis aute irure dolor in reprehenderit in voluptate velit esse cillum dolore eu</p>
    </li>
    <li>
      <svg width="6" height="6" viewBox="0 0 6 6"><rect x="0.3" y="0.3" width="5.4" height="5.4" fill="none" stroke="#0a57b5" stroke-width="0.6"/><path d="M1.2 3l1.2 1.3L4.9 1.6" fill="none" stroke="#0a57b5" stroke-width="0.9"/></svg>
      <p class="bullet-title">Lorem ipsum dolor sit amet</p>
      <p class="body-text">consectetur adipisicing elit, sed do eiusmod tempor incididunt ut labore et dolore magna aliqua. Ut enim ad minim veniam, quis nostrud exercitation ullamco laboris nisi ut aliquip ex ea commodo consequat. Duis aute irure dolor in reprehenderit in voluptate velit esse cillum dolore eu</p>
    </li>
  </ul>
  <footer class="slide-footer"><span class="footer-brand"><span class="dot"></span>KVRT</span><span class="page-no">12</span></footer>
</section>

<section class="slide col-2 row-2">
  <h2 class="slide-header">GENERAL TEXT</h2>
  <p class="general-lead caps-blue">Lorem ipsum dolor sit met consectur adipsicing elit, sed do euismod tempor incididunt ut labore et delore magna</p>
  <div class="general-rule"></div>
  <div class="general-body body-text">
    <p>Lorem ipsum dolor sit amet, consectetur adipisicing elit, sed do eiusmod tempor incididunt ut labore et dolore magna aliqua. Ut enim ad minim veniam, quis nostrud exercitation ullamco laboris nisi ut aliquip ex ea commodo consequat. Duis aute irure dolor in reprehenderit in voluptate velit esse cillum dolore eu fugiat nulla pariatur.</p>
    <p>Lorem ipsum dolor sit amet, consectetur adipisicing elit, sed do eiusmod tempor incididunt ut labore et dolore magna aliqua. Ut enim ad minim veniam, quis nostrud exercitation ullamco laboris nisi ut aliquip ex ea commodo consequat. Duis aute irure dolor in reprehenderit in voluptate velit esse cillum dolore eu</p>
  </div>
  <footer class="slide-footer"><span class="footer-brand"><span class="dot"></span>KVRT</span><span class="page-no">12</span></footer>
</section>

<section class="slide col-3 row-2">
  <h2 class="slide-header">OUR TEAM</h2>
  <p class="team-intro">dolor sit amet, consectetur adipisicing elit, sed do eiusmod tempor incididunt ut labore et dolore magna aliqua. Ut enim ad minim veniam, quis nostrud exercitation ullamco laboris nisi ut a</p>
  <article class="member" style="left:40px">
    <div class="member-photo" role="img" aria-label="Portrait photo of the president"></div>
    <h3>JONATHAN DOE</h3>
    <p class="role">President</p>
    <p class="body-text">dolor sit amet, consectetur adipisicing elit, sed do eiusmod tempor incididunt ut labore et dolore magna aliqua. Ut enim ad minim veniam, quis nostrud</p>
  </article>
  <article class="member" style="left:142px">
    <div class="member-photo" role="img" aria-label="Portrait photo of the CEO and founder"></div>
    <h3>MELANIE DOE</h3>
    <p class="role">CEO / Founder</p>
    <p class="body-text">dolor sit amet, consectetur adipisicing elit, sed do eiusmod tempor incididunt ut labore et dolore magna aliqua. Ut enim ad minim veniam, quis nostrud</p>
  </article>
  <article class="member" style="left:243px">
    <div class="member-photo" role="img" aria-label="Portrait photo of the vice president"></div>
    <h3>NATALIE DOE</h3>
    <p class="role">Vice President</p>
    <p class="body-text">dolor sit amet, consectetur adipisicing elit, sed do eiusmod tempor incididunt ut labore et dolore magna aliqua. Ut enim ad minim veniam, quis nostrud</p>
  </article>
  <footer class="slide-footer"><span class="footer-brand"><span class="dot"></span>KVRT</span><span class="page-no">12</span></footer>
</section>

<section class="slide col-1 row-3 image-slide">
  <h2>IMAGE TEXT</h2>
  <div class="image-copy">
    <h3>LOREM IPSUM DOLOR SIT MET</h3>
    <p class="body-text">Lorem ipsum dolor sit amet, consectetur adipisicing elit, sed do eiusmod tempor incididunt ut labore et dolore magna aliqua. Ut enim ad minim veniam, quis nostrud exercitation ullamco laboris nisi ut aliquip ex ea commodo consequat. Duis aute irure dolor in reprehenderit in voluptate velit esse cillum dolore eu fugiat nulla pariatur.</p>
    <p class="body-text">Lorem ipsum dolor sit amet, consectetur adipisicing elit, sed do eiusmod tempor incididunt ut labore et dolore magna aliqua. Ut enim ad minim veniam, quis nostrud exercitation ullamco laboris nisi ut aliquip ex ea commodo consequat. Duis aute irure dolor in reprehenderit in voluptate velit esse cillum dolore eu</p>
  </div>
  <div class="portrait" role="img" aria-label="Black and white photo of two smiling colleagues"></div>
  <span class="image-brand">KVRT</span>
</section>

<section class="slide col-2 row-3 section-slide" role="img" aria-label="Blue-tinted photo of a team meeting behind the section title">
  <div class="section-icon">i</div>
  <div class="section-rule"></div>
  <p class="section-title">SECTION TITLE</p>
</section>

<section class="slide col-3 row-3">
  <div class="thanks-top">
    <div class="thanks-brand"><span class="mark"></span>KVRT</div>
  </div>
  <div class="thanks-panel">
    <h2>THANK YOU</h2>
    <p class="sub">FOR YOUR TIME</p>
    <ul class="contact-list">
      <li><svg width="7" height="7" viewBox="0 0 8 8"><circle cx="4" cy="4" r="4" fill="#fff"/><path d="M4 1.6a1.5 1.5 0 0 1 1.5 1.5C5.5 4.3 4 6.3 4 6.3S2.5 4.3 2.5 3.1A1.5 1.5 0 0 1 4 1.6z" fill="#0a57b5"/></svg><span>4120 Harrow Lake Road Ste 300<br>Brookfield, Ohio 44403</span></li>
      <li><svg width="7" height="7" viewBox="0 0 8 8"><circle cx="4" cy="4" r="4" fill="#fff"/><path d="M2 3.2c0-.6 1-1 2-1s2 .4 2 1l-.6.3-.5-.5H3.1l-.5.5zM2.6 4h2.8v1.8H2.6z" fill="#0a57b5"/></svg><span>1.800.555.0143</span></li>
      <li><svg width="7" height="7" viewBox="0 0 8 8"><circle cx="4" cy="4" r="4" fill="#fff"/><rect x="2" y="2.7" width="4" height="2.8" fill="none" stroke="#0a57b5" stroke-width="0.6"/><path d="M2 2.8l2 1.5 2-1.5" fill="none" stroke="#0a57b5" stroke-width="0.6"/></svg><span>support@kvrtsys.com</span></li>
      <li><svg width="7" height="7" viewBox="0 0 8 8"><circle cx="4" cy="4" r="4" fill="#fff"/><circle cx="4" cy="4" r="2.2" fill="none" stroke="#0a57b5" stroke-width="0.5"/><path d="M1.8 4h4.4M4 1.8c-1.2 1.3-1.2 3.1 0 4.4M4 1.8c1.2 1.3 1.2 3.1 0 4.4" fill="none" stroke="#0a57b5" stroke-width="0.4"/></svg><span>www.kvrtsys.com</span></li>
    </ul>
  </div>
</section>

</body>
</html>
```